KRT World Class Organisation Poster

We are looking for ideas on how to design this poster to best capture the message we are trying to convey (KRT World Class Organisation). Make sure that these 5 statements feature on the poster.

Logo has been provided, please include in your poster design.

Please use the logo design as the inspiration for your poster layout, drawing on the DNA double helix symbol.

Also refer to the layout of the attached poster. We would like to retain the layout however it should be visually appealing - use your imagination & creativity!
Updates

Target Market(s)

internal company use only - logo provided which will need to be included.

Requirements
Must have
• The poster should be in portrait format as it will be printed in 'A3' size.

Must include the KRT logo provided - see attached file.
Nice to have
• Please use the logo design as the inspiration for your poster layout, drawing on the DNA double helix symbol.

```html
<!DOCTYPE html>
<html lang="en">
<head>
<meta charset="utf-8">
<title>KRT World Class Organisation Poster</title>
<link href="https://fonts.googleapis.com/css2?family=Roboto+Condensed:wght@300;400&family=Arimo:wght@400;700&display=swap" rel="stylesheet">
<style>
  :root {
    --page: #ffffff;
    --poster: #e3e3e3;
    --poster-light: #ececec;
    --ink: #1e1e1e;
    --body-ink: #4a4a4a;
    --line: #3a3a3a;
    --decor-dark: rgba(120,120,120,0.55);
    --decor-fade: rgba(200,200,200,0);
  }
  html, body {
    margin: 0;
    width: 1200px;
    height: 900px;
    overflow: hidden;
    background: var(--page);
  }
  .canvas {
    position: relative;
    width: 1200px;
    height: 900px;
  }
  .poster {
    position: absolute;
    left: 318px;
    top: 50px;
    width: 565px;
    height: 800px;
    background: linear-gradient(160deg, var(--poster-light), var(--poster) 60%, #dcdcdc);
    overflow: hidden;
  }
  .decor {
    position: absolute;
  }
  .decor--top-left {
    left: 0;
    top: 0;
    width: 180px;
    height: 320px;
    background: radial-gradient(ellipse at 20% 25%, var(--decor-dark), var(--decor-fade) 70%);
  }
  .decor--bottom-right {
    right: 0;
    bottom: 0;
    width: 200px;
    height: 330px;
    background: radial-gradient(ellipse at 80% 70%, var(--decor-dark), var(--decor-fade) 72%);
  }
  .headline {
    position: absolute;
    left: 0;
    top: 86px;
    width: 100%;
    text-align: center;
    font-family: "Roboto Condensed", sans-serif;
    color: var(--ink);
    margin: 0;
  }
  .headline__lead {
    display: block;
    font-weight: 300;
    font-size: 40px;
    line-height: 42px;
    letter-spacing: -1px;
  }
  .headline__main {
    display: block;
    font-weight: 400;
    font-size: 44px;
    line-height: 44px;
    letter-spacing: -1.7px;
  }
  .hex-grid {
    position: absolute;
    left: 0;
    top: 0;
  }
  .hex {
    fill: none;
    stroke: var(--line);
    stroke-width: 1;
    stroke-dasharray: 3 2.5;
  }
  .statement {
    position: absolute;
    width: 180px;
    margin: 0;
    text-align: center;
    font-family: "Arimo", sans-serif;
    font-size: 10.3px;
    line-height: 13.9px;
    color: var(--body-ink);
    transform: translateX(-50%);
  }
  .statement--key {
    font-weight: 700;
    color: var(--ink);
  }
  .statement--tight {
    line-height: 10.6px;
  }
</style>
</head>
<body>
<div class="canvas">
  <div class="poster">
    <div class="decor decor--top-left" role="img" aria-label="Grey circuit-board trace pattern"></div>
    <div class="decor decor--bottom-right" role="img" aria-label="Grey circuit-board trace pattern"></div>

    <h1 class="headline">
      <span class="headline__lead">KRT IS A</span>
      <span class="headline__main">WORLD CLASS ORGANISATION</span>
    </h1>

    <svg class="hex-grid" width="565" height="800" viewBox="318 50 565 800">
      <polygon class="hex" points="498,330 540,248 661,248 703,330 661,412 540,412"/>
      <polygon class="hex" points="660,418 702,336 824,336 866,418 824,500 702,500"/>
      <polygon class="hex" points="498,505 540,423 661,423 703,505 661,587 540,587"/>
      <polygon class="hex" points="335,590 377,508 498,508 540,590 498,672 377,672"/>
      <polygon class="hex" points="498,678 540,596 661,596 703,678 661,760 540,760"/>
    </svg>

    <p class="statement" style="left:282px; top:240px;">1. We employ<br>World Class Business<br>Systems to exceed<br>expectations by driving<br>innovation at the forefront<br>of technology.</p>

    <p class="statement" style="left:445px; top:312px;">2. We manufacture<br>using innovative World<br>Class Manufacturing<br>Processes and lean<br>technologies adapted to<br>produce safe, effective &amp;<br>reliable products to meet<br>our patients' needs.</p>

    <p class="statement statement--key" style="left:282px; top:384px; width:190px;">3. We strive to<br>be World Class<br>Colleagues who are<br>professional, motivated,<br>helpful and positive. We are<br>accountable in achieving our<br>goals. We are innovative,<br>always challenge the<br>status-quo and open<br>to new ideas.</p>

    <p class="statement statement--tight" style="left:119px; top:508px; width:190px;">4. We work with<br>World Class Service<br>Providers who are leaders<br>and innovators that challenge<br>the status-quo and focus on<br>quality excellence and<br>continuous improvement<br>to exceed customer<br>expectations.</p>

    <p class="statement" style="left:282px; top:594px;">5. We believe<br>World Class Customer<br>Service is to deliver the<br>ultimate customer<br>satisfaction every time.</p>
  </div>
</div>
</body>
</html>
```